Corporate Business Card

Very professional, Modern, Not to busy, include phone address email, website
(555) 555-0174, 61807 19th Street N, Corvane, ID 98517, marcus@kestrelbayholding.com, brelvanindustries.com

Target Market(s)

Manufacturing

Industry/Entity Type

Aero, machining, manufacturing, Off road racing

Contact Information for Business Card

Phone, address email, website

```html
<!DOCTYPE html>
<html lang="en">
<head>
<meta charset="utf-8">
<title>Brelvan Industries – Business Card</title>
<link rel="stylesheet" href="https://fonts.googleapis.com/css2?family=Poppins:wght@400;500;600;700&display=swap">
<style>
  :root {
    --brand-blue: #3c6aad;
    --brand-blue-deep: #163f86;
    --brand-blue-dark: #0f2f6a;
    --brand-red: #e0393e;
    --ink-grey: #5d5f63;
    --card-white: #f4f4f4;
    --page-bg: #2a2b2e;
  }
  * { box-sizing: border-box; margin: 0; padding: 0; }
  html, body {
    width: 1200px; height: 900px; overflow: hidden;
    background: var(--page-bg);
    font-family: "Poppins", Arial, sans-serif;
  }
  .sheet {
    width: 1200px; height: 900px;
    display: flex; flex-direction: column;
    align-items: center; justify-content: center; gap: 40px;
  }
  .card {
    position: relative;
    width: 630px; height: 360px;
    overflow: hidden;
    box-shadow: 0 10px 30px rgba(0,0,0,.45);
  }

  /* Front */
  .card-front { background: var(--card-white); }
  .edge-band {
    position: absolute; left: 0; top: 0; width: 16px; height: 100%;
    background: linear-gradient(to bottom, var(--brand-blue-deep) 0 44%, var(--brand-red) 44% 100%);
  }
  .identity { position: absolute; left: 52px; top: 118px; }
  .person-name {
    color: var(--brand-blue); font-weight: 600; font-size: 22px; line-height: 1.15;
  }
  .person-title {
    color: var(--brand-red); font-weight: 500; font-size: 15px; margin-top: 1px;
  }
  .rule {
    position: absolute; left: 52px; top: 176px; width: 470px; height: 1px;
    background: var(--brand-red);
  }
  .contact-list {
    position: absolute; left: 52px; top: 190px; list-style: none;
    color: var(--ink-grey); font-size: 15px; line-height: 25px;
  }
  .contact-list li { display: flex; align-items: center; gap: 9px; }
  .contact-list svg { width: 14px; height: 14px; fill: var(--brand-blue); flex: none; }
  .brand-lockup {
    position: absolute; right: 48px; top: 112px;
    display: flex; align-items: center; gap: 10px;
  }
  .brand-mark { width: 13px; height: 13px; background: var(--brand-red); }
  .brand-name {
    color: var(--brand-blue); font-weight: 600; font-size: 25px; letter-spacing: .3px;
  }
  .address {
    position: absolute; right: 48px; bottom: 36px; text-align: right;
    color: var(--ink-grey); font-size: 15px; line-height: 23px; font-style: normal;
  }

  /* Back */
  .card-back {
    background: radial-gradient(ellipse at 35% 30%, var(--brand-blue-deep), var(--brand-blue-dark));
    display: flex; align-items: center; justify-content: center; gap: 14px;
  }
  .card-back .brand-mark { width: 18px; height: 18px; }
  .card-back .brand-name { color: #ffffff; font-size: 40px; }
</style>
</head>
<body>
<main class="sheet">
  <section class="card card-front" aria-label="Business card front">
    <div class="edge-band"></div>

    <div class="identity">
      <p class="person-name">Dana Whitcomb</p>
      <p class="person-title">Vice President</p>
    </div>

    <div class="brand-lockup">
      <span class="brand-mark"></span>
      <span class="brand-name">Brelvan Industries</span>
    </div>

    <div class="rule"></div>

    <ul class="contact-list">
      <li>
        <svg viewBox="0 0 24 24" aria-hidden="true"><path d="M6.6 10.8a15.1 15.1 0 0 0 6.6 6.6l2.2-2.2a1 1 0 0 1 1-.25 11.4 11.4 0 0 0 3.6.57 1 1 0 0 1 1 1V20a1 1 0 0 1-1 1A17 17 0 0 1 3 4a1 1 0 0 1 1-1h3.5a1 1 0 0 1 1 1c0 1.25.2 2.45.57 3.57a1 1 0 0 1-.25 1z"/></svg>
        (555) 555-0174
      </li>
      <li>
        <svg viewBox="0 0 24 24" aria-hidden="true"><path d="M2 5h20v14H2z M3 6l9 7 9-7" stroke="#f4f4f4" stroke-width="1.5"/></svg>
        marcus@kestrelbayholding.com
      </li>
      <li>
        <svg viewBox="0 0 24 24" aria-hidden="true"><circle cx="12" cy="12" r="10"/><path d="M2 12h20M12 2c3 3 3 17 0 20M12 2c-3 3-3 17 0 20" stroke="#f4f4f4" stroke-width="1.4" fill="none"/></svg>
        www.brelvanindustries.com
      </li>
    </ul>

    <address class="address">
      61807 19th Street N,<br>Corvane, ID 98517,
    </address>
  </section>

  <section class="card card-back" aria-label="Business card back">
    <span class="brand-mark"></span>
    <span class="brand-name">Brelvan Industries</span>
  </section>
</main>
</body>
</html>
```